Tirolex

We need a business card for our company is a holding for different business all are different we try to have some air of relax and fun in our projects we add pictures of the office to give you an idea od the mood of the business

Business

```html
<!DOCTYPE html>
<html lang="en">
<head>
<meta charset="utf-8">
<title>Tirolex business card</title>
<link rel="stylesheet" href="https://fonts.googleapis.com/css2?family=Open+Sans:wght@400;700;800&display=swap">
<style>
  :root {
    --backdrop: #d9d6d2;
    --card-black: #1b1b1b;
    --card-edge: #111111;
    --gloss-black: #2a2a2a;
    --brand-yellow: #f2e600;
    --brand-brown: #5a3416;
    --name-yellow: #f4e21a;
    --text-white: #f2f2f2;
    --divider: rgba(255,255,255,0.12);
  }
  * { box-sizing: border-box; margin: 0; padding: 0; }
  html, body {
    width: 1200px; height: 805px; overflow: hidden;
    background: var(--backdrop);
    font-family: "Open Sans", Arial, sans-serif;
  }
  .canvas {
    position: relative; width: 1200px; height: 805px;
  }
  .card {
    position: absolute; top: 248px;
    width: 540px; height: 309px;
    background: var(--card-black);
    border-radius: 3px;
    box-shadow: 0 10px 24px rgba(0,0,0,0.25);
    overflow: hidden;
  }
  /* Back side */
  .card-back { left: 40px; }
  .back-name {
    position: absolute; left: 0; right: 0; top: 112px;
    text-align: center;
    font-weight: 800; font-size: 68px; letter-spacing: -2px;
    color: var(--gloss-black);
  }
  /* Front side */
  .card-front { left: 620px; }
  .brand-panel {
    position: absolute; left: 34px; top: 30px;
    width: 250px; height: 250px;
    background: var(--brand-yellow);
  }
  .brand-name {
    position: absolute; left: 20px; top: 22px;
    font-weight: 800; font-size: 54px; letter-spacing: -2px; line-height: 1;
    color: var(--brand-brown);
  }
  .divider {
    position: absolute; left: 302px; top: 118px;
    width: 1px; height: 160px; background: var(--divider);
  }
  .contact {
    position: absolute; left: 314px; top: 96px; right: 16px;
    color: var(--text-white);
  }
  .person-name {
    font-weight: 700; font-size: 24px; line-height: 1.1;
    color: var(--name-yellow);
  }
  .person-role { font-size: 13px; margin-bottom: 10px; }
  .address { font-size: 13px; line-height: 1.35; margin-bottom: 4px; }
  .contact-list { list-style: none; font-size: 13px; line-height: 1.5; }
  .contact-list li { display: flex; align-items: center; gap: 7px; }
  .contact-list svg { width: 11px; height: 11px; fill: var(--name-yellow); flex: none; }
</style>
</head>
<body>
<main class="canvas">

  <section class="card card-back" aria-label="Card back">
    <div class="back-name">Tirolex</div>
  </section>

  <section class="card card-front" aria-label="Card front">
    <div class="brand-panel">
      <span class="brand-name">Tirolex</span>
    </div>
    <div class="divider"></div>
    <div class="contact">
      <h1 class="person-name">Daniel R. Holt</h1>
      <p class="person-role">Managing Member</p>
      <p class="address">2280 Harbor Lane,<br>Fresno, CA 93721</p>
      <ul class="contact-list">
        <li><svg viewBox="0 0 12 12" aria-hidden="true"><path d="M2.5 1l2 2.2-1 1.3c.7 1.5 1.8 2.6 3.3 3.3l1.3-1 2.2 2-1.2 1.9C5 10.3 1.7 7 .7 2.3z"/></svg>(559) 410-2231</li>
        <li><svg viewBox="0 0 12 12" aria-hidden="true"><path d="M3 1h5l1 1v2H3zM1 5h10v5H9V8H3v2H1zM3 9h6v2H3z"/></svg>(559) 410-2232</li>
        <li><svg viewBox="0 0 12 12" aria-hidden="true"><path d="M3 0h6v12H3zM4 1.5v8h4v-8z"/></svg>(559) 803-4417</li>
        <li><svg viewBox="0 0 12 12" aria-hidden="true"><path d="M0 2h12v8H0zM1 3l5 3.5L11 3v-.2H1z"/></svg>daniel@tirolexgroup.com</li>
        <li><svg viewBox="0 0 12 12" aria-hidden="true"><path d="M6 0a6 6 0 100 12A6 6 0 006 0zm0 1.2c.8.9 1.3 2.3 1.4 4.2H4.6C4.7 3.5 5.2 2.1 6 1.2zM1.3 6.6h2.3c.1 1.6.5 3 1.1 4A4.8 4.8 0 011.3 6.6zm0-1.2a4.8 4.8 0 013.4-4c-.6 1-1 2.4-1.1 4zm3.3 1.2h2.8C7.3 8.5 6.8 9.9 6 10.8c-.8-.9-1.3-2.3-1.4-4.2zm3.8 0h2.3a4.8 4.8 0 01-3.4 4c.6-1 1-2.4 1.1-4zm0-1.2c-.1-1.6-.5-3-1.1-4a4.8 4.8 0 013.4 4z"/></svg>www.tirolexgroup.com</li>
      </ul>
    </div>
  </section>

</main>
</body>
</html>
```